Design Creative Banner or Gif Ads. 3 Designs To Be Selected

Come up with some creative banner ads for stonewell.co.nz

*At least 3 different winning banners will be chosen*

Please provide banner ads / gif ads in common google ads / website banner formats.

They can be gif or static but must stand out while still maintaining clear clean text and visuals, with a premium professional feel (please avoid clip art or anything that gives a cheap message).

Please keep in mind that these will likely be small ads so text needs to be large and if there's there a lot of text then use multiple frames/ pages as submit as a gif.

Style
Minimal & clean lines
Architectural or realistic images
Avoid cartoon styles, clipart, or anything that looks cheap

Font
Nexa or Montserrat or similar

Tone
Premium, serious, trustworthy — fits new builds

Colours
Option 1: Deep Navy (trust & quality) & lighter blues and warm grey
Option 2: Open to bright colours to help the ads stand out, such as (but not limited to) bright pink with black, yellow, fluorescent green, provided the messaging is still done professionally.
Our logo is attached (Stone Well Logo)

Display Sizes
Ad specs for file sizes should be file formats like JPEG, GIF, and PNG, with animations limited to a max of 30 seconds or less.
We will need several different ad sizes provided for each of the 3 selected winning designs.

• Medium Rectangle: 300 × 250 pixels
• Leaderboard: 728 × 90 pixels
• Desktop Banner ad image: (640x360 pixels)
• Desktop Banner ad image 2: (300x600 pixels)
• Possibly one or two other sizes

Flexibility to be creative
The ad text, words, upper/lower case, layout, colour, theme, and images can be adjusted to how you think it will look best. The follow example ads are just examples of what we are after but we are keen to see what you can create.

Recommendations at this point:
1. Avoid text heavy
2. Looking for more Gif ads
3. Imaging: if possible use real stock photo's rather than AI

Themes:

1
Building Soon? Start Here
Free Build Planning Pack:
✓ Build Cost Calculator
✓ Hidden Cost Checklist
✓ Builder Comparison Guide
Build With Confidence
Download Free

2
Before You Choose A Builder
Compare Price, Scope, Risk & Value
Avoid Costly Mistakes
Choose The Right Builder With Confidence
Download The Free Guide

3
Planning A New Build?
Avoid These Common Mistakes:
✗ Hidden Exclusions
✗ Missing Scope
✗ Unrealistic Allowances
✗ Budget Blowouts
Download The Free Guide

4
Before You Buy Land
Know what it could cost to build.
Avoid Costly Building Mistakes
Download Our Free Guides

5
Know Your Build Budget?
• Free Build Cost Calculator
• Hidden Cost Checklist
• Build Planning Tools
Calculate Costs (Download)

Target Market(s)

Landowners looking to build

Industry/Entity Type

Building

Font styles to use
Other font styles liked:
• Nexa or Montserrat or similar

Requirements
Should not have
• Avoid cartoon styles, clipart, or anything that looks cheap

```html
<!DOCTYPE html>
<html lang="en">
<head>
<meta charset="UTF-8">
<title>Stone Well – Before You Choose A Builder</title>
<link rel="stylesheet" href="https://fonts.googleapis.com/css2?family=Montserrat:wght@500;600;700&display=swap">
<style>
  :root {
    --bg: #000000;
    --ink: #ffffff;
    --accent: #e6f51d;
    --button: #e4f322;
    --button-ink: #111111;
    --photo-a: #24272b;
    --photo-b: #6d6a64;
    --photo-c: #a88764;
    --photo-d: #d9dcdf;
  }
  * { margin: 0; padding: 0; box-sizing: border-box; }
  html, body {
    width: 1200px;
    height: 675px;
    overflow: hidden;
    background: var(--bg);
  }
  .banner {
    position: relative;
    width: 1200px;
    height: 675px;
    background: var(--bg);
    font-family: "Montserrat", sans-serif;
    color: var(--ink);
    overflow: hidden;
  }
  .house-photo {
    position: absolute;
    left: 560px;
    top: 155px;
    width: 640px;
    height: 520px;
    background:
      radial-gradient(ellipse at 70% 20%, var(--photo-d) 0%, transparent 30%),
      radial-gradient(ellipse at 62% 58%, var(--photo-c) 0%, transparent 45%),
      linear-gradient(160deg, var(--photo-b) 0%, var(--photo-a) 70%);
    -webkit-mask-image: linear-gradient(90deg, transparent 0%, #000 12%);
    mask-image: linear-gradient(90deg, transparent 0%, #000 12%);
  }
  .brand {
    position: absolute;
    left: 879px;
    top: 54px;
    height: 57px;
    display: flex;
    align-items: center;
    gap: 14px;
  }
  .brand-mark {
    width: 40px;
    height: 40px;
    background: var(--accent);
    flex: none;
  }
  .brand-name {
    font-size: 30px;
    font-weight: 600;
    color: var(--ink);
    line-height: 1;
    white-space: nowrap;
  }
  .eyebrow {
    position: absolute;
    left: 46px;
    top: 97px;
    font-size: 30px;
    font-weight: 600;
  }
  .headline {
    position: absolute;
    left: 26px;
    top: 153px;
    font-size: 109px;
    font-weight: 700;
    color: var(--accent);
    line-height: 1;
    letter-spacing: 0.5px;
  }
  .criteria {
    position: absolute;
    left: 46px;
    top: 291px;
    font-size: 29px;
    font-weight: 500;
  }
  .pitfalls {
    position: absolute;
    left: 46px;
    top: 388px;
    list-style: none;
  }
  .pitfalls li {
    display: flex;
    align-items: center;
    font-size: 19.5px;
    font-weight: 500;
    height: 27.5px;
  }
  .pitfalls li::before {
    content: "";
    width: 7px;
    height: 7px;
    background: var(--accent);
    margin-right: 23px;
  }
  .cta {
    position: absolute;
    left: 60px;
    top: 555px;
    width: 1080px;
    height: 92px;
    border-radius: 20px;
    background: var(--button);
    color: var(--button-ink);
    display: flex;
    align-items: center;
    justify-content: center;
    font-size: 32px;
    font-weight: 600;
    text-decoration: none;
  }
</style>
</head>
<body>
  <div class="banner">
    <div class="house-photo" role="img" aria-label="Modern three-storey architect-designed home at dusk with glass balconies, timber cladding and warm downlights"></div>

    <div class="brand">
      <span class="brand-mark"></span>
      <span class="brand-name">Stone Well</span>
    </div>

    <p class="eyebrow">Before You Choose A Builder</p>
    <h1 class="headline">COMPARE</h1>
    <p class="criteria">Price - Scope - Risk - Value</p>

    <ul class="pitfalls">
      <li>Hidden Exclusion</li>
      <li>Missing Scope</li>
      <li>Unrealistic Allowance</li>
      <li>Budget Blowouts</li>
    </ul>

    <a class="cta" href="#">DOWNLOAD FREE GUIDE</a>
  </div>
</body>
</html>
```